Sam Greenfield Billboard

**Task Description: Billboard Design for Self Storage Facility**

**Objective:**
Design a captivating billboard to promote our self-storage facility with a focus on our convenient location and online rental capabilities.

**Key Messages to Include:**
1. **Location Emphasis:** Highlight that our facility is located right beside the billboard (maybe by using an arrow pointing left).
2. **Online Rental Convenience:** Feature prominently that customers can "Rent Online Anytime!” or that we are "Always Open Online!"

**Target Audience:**
- Local residents looking for convenient self-storage solutions.
- Businesses needing storage space accessible around the clock.

**Design Elements:**
1. **Visual Impact:** Eye-catching graphics and colors that stand out against the surroundings.
2. **Clear Text:** Bold and concise messaging that can be read and understood quickly.
3. **Contact Information:** Include our phone number and website URL for easy access to further information.

**Additional Information:**
- Billboard dimensions: 12 ft. x 24 ft.
- Preferred color scheme: Bright and attention-grabbing, but professional.
- Branding: Incorporate our logo and brand colors to maintain consistency.

**Deliverables:**
- High-resolution digital file compatible with billboard printing specifications.
- Consider mockups or visualizations for presentation purposes.

Please note that I have attached current logos/graphics that we would love to incorporate into the billboard as well as a picture of our current billboard. Our logo (Sam Greenfield Self Storage - SG navy.png) MUST be incorporated into the billboard. Also feel free to add any of the current descriptions from the picture of our current billboard into the design. Instead of using "Climate Controlled" use "Temperature Controlled". Thank you for your attention to these details. We look forward to reviewing your proposed design!

```html
<!DOCTYPE html>
<html lang="en">
<head>
<meta charset="utf-8">
<title>Sam Greenfield Billboard</title>
<link href="https://fonts.googleapis.com/css2?family=Montserrat:wght@600;700;800&display=swap" rel="stylesheet">
<style>
  :root {
    --page-bg: #aeaaaa;
    --board-dark: #0a1424;
    --board-mid: #0d2a5a;
    --board-glow: #1a5bb8;
    --circuit-cyan: #3fc4e8;
    --text-white: #ffffff;
    --brand-navy: #1d2a5c;
    --brand-border: #1d2a5c;
    --device-frame: #1b1d22;
    --device-screen-top: #e9edf3;
    --device-screen-mid: #4a5566;
  }
  html, body {
    margin: 0;
    padding: 0;
    width: 1200px;
    height: 1200px;
    overflow: hidden;
    background: var(--page-bg);
    font-family: "Montserrat", Arial, sans-serif;
  }
  .canvas {
    position: relative;
    width: 1200px;
    height: 1200px;
  }
  .billboard {
    position: absolute;
    left: 90px;
    top: 345px;
    width: 1020px;
    height: 510px;
    overflow: hidden;
    background: linear-gradient(100deg, var(--board-dark) 0%, var(--board-dark) 38%, var(--board-mid) 70%, var(--board-glow) 100%);
  }
  .circuit-art {
    position: absolute;
    left: 420px;
    top: 0;
    width: 600px;
    height: 510px;
    background:
      radial-gradient(ellipse at 70% 35%, rgba(63,196,232,0.35), transparent 60%),
      radial-gradient(ellipse at 85% 80%, rgba(63,196,232,0.25), transparent 55%);
  }
  .device-preview {
    position: absolute;
    left: 162px;
    top: 57px;
    width: 165px;
    height: 320px;
    border-radius: 14px;
    background: var(--device-frame);
    box-sizing: border-box;
    padding: 8px;
  }
  .device-preview .screen {
    width: 100%;
    height: 100%;
    border-radius: 6px;
    background: linear-gradient(180deg, var(--device-screen-top) 0%, var(--device-screen-top) 10%, var(--device-screen-mid) 12%, #2e3744 40%, var(--device-screen-top) 42%, #dfe4ea 100%);
  }
  .headline {
    position: absolute;
    right: 79px;
    top: 140px;
    margin: 0;
    text-align: right;
    color: var(--text-white);
    font-weight: 700;
    font-size: 74px;
    line-height: 82px;
    letter-spacing: 0.5px;
  }
  .tagline {
    position: absolute;
    left: 80px;
    top: 406px;
    margin: 0;
    color: var(--text-white);
    font-weight: 600;
    font-size: 27px;
    letter-spacing: 0.3px;
  }
  .brand-mark {
    position: absolute;
    left: 714px;
    top: 401px;
    width: 232px;
    height: 75px;
    box-sizing: border-box;
    background: var(--text-white);
    border: 2px solid var(--brand-border);
    display: flex;
    flex-direction: column;
    align-items: center;
    justify-content: center;
    color: var(--brand-navy);
    font-weight: 700;
    text-align: center;
  }
  .brand-mark .brand-name {
    font-size: 21px;
    line-height: 24px;
    letter-spacing: 0.5px;
  }
  .brand-mark .brand-sub {
    font-size: 12px;
    line-height: 16px;
    letter-spacing: 3px;
  }
</style>
</head>
<body>
  <div class="canvas">
    <section class="billboard">
      <div class="circuit-art" role="img" aria-label="Glowing blue circuit-board lines and light points"></div>
      <div class="device-preview" role="img" aria-label="Tablet showing the storage rental website">
        <div class="screen"></div>
      </div>
      <h1 class="headline">SELF STORAGE<br>FACILITY</h1>
      <p class="tagline">ALWAYS OPEN ONLINE!</p>
      <div class="brand-mark">
        <span class="brand-name">SAM GREENFIELD</span>
        <span class="brand-sub">SELF STORAGE</span>
      </div>
    </section>
  </div>
</body>
</html>
```